Strong, modern, clean Business Card design

Looking for a stunning, but CLEAN business card design. While we are a faith-based organization, we do NOT want this to look religious.

Industry/Entity Type

Non-Profit

Contact Information for Business Card

Dale Munroe | Lead Pastor
dale@BrightHarvestHope.org
970-555-0148
PO Box 7316
Fernvale, NV 80571

Font styles to use
Serif
Sans Serif

Requirements
Should not have
• Religious imagery or symbolism

```html
<!DOCTYPE html>
<html lang="en">
<head>
<meta charset="utf-8">
<title>Bright Harvest — Business Card</title>
<link href="https://fonts.googleapis.com/css2?family=Open+Sans:wght@400;600&display=swap" rel="stylesheet">
<style>
  :root {
    --brand-blue: #4d7a94;
    --ink: #454545;
    --band-grey: #bfbfbf;
    --paper: #ffffff;
    --backdrop: #ffffff;
  }
  html, body {
    margin: 0;
    padding: 0;
    width: 1200px;
    height: 1200px;
    overflow: hidden;
    background: var(--backdrop);
    font-family: "Open Sans", Arial, sans-serif;
  }
  .card {
    position: absolute;
    left: 180px;
    top: 360px;
    width: 840px;
    height: 480px;
    background: var(--paper);
    outline: 1px solid #e6e6e6;
    overflow: hidden;
  }
  .card > * { position: absolute; margin: 0; }
  .brand-name {
    left: 72px;
    top: 62px;
    font-size: 38px;
    font-weight: 600;
    letter-spacing: 2px;
    color: var(--brand-blue);
    white-space: nowrap;
  }
  .brand-mark {
    left: 664px;
    top: 43px;
    width: 128px;
    height: 128px;
    border-radius: 20px;
    background: var(--brand-blue);
  }
  .person-name {
    left: 60px;
    top: 234px;
    font-size: 42px;
    font-weight: 600;
    color: var(--brand-blue);
    line-height: 1;
    letter-spacing: -0.5px;
    white-space: nowrap;
  }
  .person-role {
    left: 60px;
    top: 288px;
    font-size: 26px;
    font-weight: 400;
    color: var(--ink);
    line-height: 1;
    white-space: nowrap;
  }
  .role-rule {
    left: 242px;
    top: 306px;
    width: 550px;
    height: 3px;
    background: var(--brand-blue);
  }
  .contact-list {
    left: 58px;
    top: 338px;
    list-style: none;
    padding: 0;
    font-size: 21px;
    color: var(--ink);
    letter-spacing: 0.4px;
  }
  .contact-list li {
    display: flex;
    align-items: center;
    height: 28.5px;
    white-space: nowrap;
  }
  .contact-list svg {
    width: 20px;
    height: 20px;
    margin-right: 16px;
    fill: var(--brand-blue);
  }
  .contact-list .domain { color: var(--brand-blue); font-weight: 600; }
  .mail-icon {
    left: 766px;
    top: 337px;
    width: 28px;
    height: 22px;
  }
  .postal-address {
    right: 48px;
    top: 370px;
    text-align: right;
    font-style: normal;
    font-size: 18px;
    line-height: 24px;
    color: var(--ink);
    letter-spacing: 0.8px;
    white-space: nowrap;
  }
  .footer-bands {
    left: 0;
    top: 440px;
    width: 840px;
    height: 40px;
  }
</style>
</head>
<body>
  <main class="card">
    <p class="brand-name">BRIGHT HARVEST</p>
    <div class="brand-mark"></div>

    <h1 class="person-name">DALE MUNROE</h1>
    <p class="person-role">LEAD PASTOR</p>
    <div class="role-rule"></div>

    <ul class="contact-list">
      <li>
        <svg viewBox="0 0 20 20" aria-hidden="true"><path d="M6 1h8a2 2 0 0 1 2 2v14a2 2 0 0 1-2 2H6a2 2 0 0 1-2-2V3a2 2 0 0 1 2-2zm0 3v10h8V4zm4 11.2a1.1 1.1 0 1 0 0 2.2 1.1 1.1 0 0 0 0-2.2z"/></svg>
        555-555-0148
      </li>
      <li>
        <svg viewBox="0 0 20 20" aria-hidden="true"><path d="M1 4h18v1.5l-9 6-9-6zM1 7.5l9 6 9-6V16H1z"/></svg>
        dale@BrightHarvestHope.org
      </li>
      <li>
        <svg viewBox="0 0 20 20" aria-hidden="true"><path d="M11.5 1.5a7 7 0 1 1-4.6 12.3L2.6 18.1 1.4 16.9l4.3-4.3A7 7 0 0 1 11.5 1.5zm0 2a5 5 0 1 0 0 10 5 5 0 0 0 0-10z"/></svg>
        <span>www.<span class="domain">BrightHarvestHope</span>.org</span>
      </li>
    </ul>

    <svg class="mail-icon" viewBox="0 0 28 22" aria-hidden="true">
      <path d="M2 20 L14 2 L26 20 Z M14 2 L11 20" fill="none" stroke="var(--brand-blue)" stroke-width="1.6" stroke-linejoin="round"/>
    </svg>
    <address class="postal-address">PO Box 7316<br>Fernvale, NV 80571</address>

    <svg class="footer-bands" viewBox="0 0 840 40" aria-hidden="true">
      <rect x="0" y="26" width="502" height="11" fill="var(--band-grey)"/>
      <polygon points="536,6 840,6 840,40 489,40" fill="var(--brand-blue)"/>
    </svg>
  </main>
</body>
</html>
```